MK Tallow Insurance - Aviation

We are wanting to have new business cards designed for our new aviation division. We currently have business cards for the other business (attached). We would like to use the same colors and have the logo somewhere on the business card along with a small, single engine airplane, maybe in the background but would like it to be different than the original and more focused on aviation. Also wondering if there is a way to do laser cut and make the business card in the shape of an airplane? Just some different ideas that make it stand out.

Target Market(s)

Pilots

Industry/Entity Type

Insurance

Contact Information for Business Card

We would like to use the same colors and have the logo somewhere on the business card along with a small, single engine airplane, maybe in the background but would like it to be different than the original and more focused on aviation. Also wondering if there is a way to do laser cut and make the business card in the shape of an airplane? Just some different ideas that make it stand out.

Requirements
Must have
• A small, single engine airplane

```html
<!DOCTYPE html>
<html lang="en">
<head>
<meta charset="utf-8">
<title>MK Tallow Insurance – Aviation Business Card</title>
<link href="https://fonts.googleapis.com/css2?family=Poppins:wght@300;400;600;700&display=swap" rel="stylesheet">
<style>
  :root {
    --brand-red: #c8001e;
    --ink-dark: #333333;
    --logo-gray: #555555;
    --backdrop: #e6e6e6;
    --card-white: #ffffff;
    --sky-top: #dfe7ee;
    --sky-mid: #eef2f4;
    --ground: #d9ddd6;
  }
  * { margin: 0; padding: 0; box-sizing: border-box; }
  html, body { width: 1200px; height: 1200px; overflow: hidden; }
  body {
    background: var(--backdrop);
    font-family: "Poppins", sans-serif;
    position: relative;
  }
  .card {
    position: absolute;
    left: 254px;
    width: 696px;
    background: var(--card-white);
    overflow: hidden;
  }
  .card--front { top: 187px; height: 387px; }
  .card--back { top: 592px; height: 386px; }

  .band {
    position: absolute;
    left: 0;
    width: 100%;
    background: var(--brand-red);
  }
  .band--top { top: 0; height: 22px; }
  .band--bottom { top: 322px; height: 65px; }

  .brand-name {
    position: absolute;
    color: var(--logo-gray);
    font-weight: 400;
    white-space: nowrap;
    letter-spacing: 0.5px;
    display: flex;
    align-items: center;
    gap: 8px;
    transform: translateX(-50%);
  }
  .brand-dot {
    width: 12px; height: 12px;
    border-radius: 50%;
    background: var(--brand-red);
  }
  .card--front .brand-name { left: 179px; top: 185px; font-size: 20px; }

  .contact-block {
    position: absolute;
    left: 347px;
    top: 121px;
    height: 138px;
    border-left: 6px solid var(--brand-red);
    padding-left: 10px;
  }
  .contact-name {
    font-size: 25px; font-weight: 600; color: var(--ink-dark); line-height: 1.1; margin-top: -2px;
  }
  .contact-title {
    font-size: 19px; font-weight: 300; color: var(--brand-red); line-height: 1.3;
  }
  .contact-phone {
    font-size: 32px; font-weight: 700; color: var(--brand-red); line-height: 1; margin-top: 24px;
  }
  .contact-email {
    font-size: 22px; font-weight: 600; color: var(--brand-red); line-height: 1.2; margin-top: 6px;
  }

  .office-info {
    position: absolute;
    left: 0; top: 322px; width: 100%; height: 65px;
    color: #fff; font-weight: 600; font-size: 16px;
    display: flex; flex-direction: column; align-items: center; justify-content: center; gap: 2px;
  }
  .office-row { display: flex; align-items: center; gap: 6px; }
  .office-row .gap { width: 14px; }
  .office-row svg { width: 15px; height: 15px; }

  .aircraft-photo {
    position: absolute;
    left: 0; top: 21px; width: 100%; height: 365px;
    background: linear-gradient(180deg, var(--sky-top) 0%, var(--sky-mid) 55%, #e8ebe6 75%, var(--ground) 100%);
  }
  .logo-strip {
    position: absolute;
    left: 0; top: 119px; width: 100%; height: 147px;
    background: rgba(255,255,255,0.72);
  }
  .card--back .brand-name { left: 348px; top: 175px; font-size: 28px; }
  .card--back .brand-dot { width: 16px; height: 16px; }
</style>
</head>
<body>
  <section class="card card--front">
    <div class="band band--top"></div>
    <div class="brand-name"><span class="brand-dot"></span>MK TALLOW INSURANCE</div>
    <div class="contact-block">
      <p class="contact-name">Dana Whitfield</p>
      <p class="contact-title">Principal Agent</p>
      <p class="contact-phone">555-218-0473</p>
      <p class="contact-email">dana@mktallow.com</p>
    </div>
    <div class="band band--bottom"></div>
    <div class="office-info">
      <div class="office-row">
        <svg viewBox="0 0 16 16"><circle cx="8" cy="8" r="7" fill="#fff"/><path d="M1 8h14M8 1c-3 3-3 11 0 14M8 1c3 3 3 11 0 14" stroke="#c8001e" stroke-width="1.2" fill="none"/></svg>
        <span>www.mktallowins.com</span>
        <span class="gap"></span>
        <svg viewBox="0 0 16 16"><circle cx="8" cy="8" r="7" fill="#fff"/><path d="M5.5 4.5l1.5-.5 1 2-1 .8c.4 1 1.2 1.8 2.2 2.2l.8-1 2 1-.5 1.5c-3 0-6-3-6-6z" fill="#c8001e"/></svg>
        <span>555-306-1192</span>
      </div>
      <div class="office-row">
        <svg viewBox="0 0 16 16"><path d="M8 1a5 5 0 0 1 5 5c0 4-5 9-5 9S3 10 3 6a5 5 0 0 1 5-5z" fill="#fff"/><circle cx="8" cy="6" r="2" fill="#c8001e"/></svg>
        <span>82 Harlow Parkway Brenton, Texas 75012</span>
      </div>
    </div>
  </section>

  <section class="card card--back">
    <div class="band band--top"></div>
    <div class="aircraft-photo" role="img" aria-label="Photo of a small single engine airplane flying over open countryside under a pale sky"></div>
    <div class="logo-strip"></div>
    <div class="brand-name"><span class="brand-dot"></span>MK TALLOW INSURANCE</div>
  </section>
</body>
</html>
```